Flyer Design Dental Office Grand Opening offer

Dental office.

Grand opening flyer. Offer Exam + cleaning + xrays.
special: free teeth whitening ($200 value)

Target Market(s)

Middle class people around Huntington Beach.

Industry/Entity Type

Dental Clinic

Colors
cfeae6
86cfc6
fac994
fee18a
e667a6

Requirements
Must have
• Do not change my existing logo
Nice to have
• Have some appealing picture/design to catch the eye, but not too flashy
Should not have
• No cartoon kind of design

```html
<!DOCTYPE html>
<html lang="en">
<head>
<meta charset="utf-8">
<title>Daybreak Dental – Grand Opening</title>
<link rel="stylesheet" href="https://fonts.googleapis.com/css2?family=Anton&family=Arimo:wght@400;700&family=Roboto+Condensed:wght@400;700&display=swap">
<style>
  :root {
    --orange: #f26522;
    --orange-soft: #f5915f;
    --teal: #00a0b0;
    --sky-top: #8fd3ea;
    --sky-bottom: #d6f1f7;
    --ring: #cfe8ee;
    --map: #d9dcd6;
    --ink: #1e1e1e;
    --paper: #ffffff;
    --stage: #eceae6;
  }
  * { margin: 0; padding: 0; box-sizing: border-box; }
  html, body { width: 1054px; height: 1200px; overflow: hidden; background: var(--stage); }
  .flyer {
    position: absolute; left: 60px; top: 0;
    width: 934px; height: 1200px;
    background: var(--paper); overflow: hidden;
    font-family: "Arimo", Arial, sans-serif;
  }
  .hero-photo {
    position: absolute; left: 0; top: 0; width: 934px; height: 469px;
    background: linear-gradient(110deg, var(--sky-top) 0%, var(--sky-bottom) 45%, #f1d2bf 70%, #e8bda4 100%);
  }
  .accent-band {
    position: absolute; left: 0; top: 469px; width: 934px; height: 48px;
    background: var(--orange-soft);
  }
  .map-badge {
    position: absolute; left: 41px; top: 392px; width: 310px; height: 310px;
    border-radius: 50%; background: var(--ring);
    display: flex; align-items: center; justify-content: center;
  }
  .map-badge .map-frame {
    width: 270px; height: 270px; border-radius: 50%; background: var(--paper);
    display: flex; align-items: center; justify-content: center;
  }
  .map-badge .map-area {
    width: 260px; height: 260px; border-radius: 50%;
    background: radial-gradient(circle at 45% 45%, #e6e8e2, var(--map));
  }
  .brand {
    position: absolute; left: 414px; top: 560px; width: 389px;
    display: flex; align-items: center; justify-content: flex-end; gap: 14px;
  }
  .brand .brand-mark { width: 40px; height: 40px; background: var(--teal); }
  .brand .brand-name {
    font-family: "Arimo", Arial, sans-serif; font-weight: 700;
    font-size: 44px; color: var(--teal); letter-spacing: 1px; white-space: nowrap;
  }
  .brand-doctor {
    position: absolute; left: 414px; top: 659px; width: 389px;
    text-align: right; font-size: 16px; color: var(--ink);
  }
  .headline {
    position: absolute; left: 52px; color: var(--orange);
    font-family: "Anton", Impact, sans-serif; line-height: 1;
    transform-origin: left top;
  }
  .headline.grand { top: 772px; font-size: 118px; transform: scaleX(0.98); }
  .headline.opening { top: 894px; font-size: 100px; transform: scaleX(0.93); }
  .offer {
    position: absolute; left: 417px; display: flex; align-items: center;
  }
  .offer .offer-key {
    font-family: "Anton", Impact, sans-serif; color: var(--teal); line-height: 1;
  }
  .offer .offer-text { color: var(--orange); font-size: 30px; line-height: 1.25; }
  .offer .offer-note { font-size: 16px; }
  .offer.exam { top: 718px; }
  .offer.exam .offer-key { font-size: 100px; width: 193px; }
  .offer.bleach { top: 854px; }
  .offer.bleach .offer-key { font-size: 96px; width: 193px; }
  .offer.bleach .offer-note { display: block; margin-top: 14px; }
  .offer.plans { top: 992px; }
  .offer.plans .offer-key { font-size: 52px; width: 236px; }
  .offer.plans .offer-text { font-size: 28px; }
  .divider {
    position: absolute; left: 417px; width: 478px; height: 0;
    border-top: 2px dotted #8a8a8a;
  }
  .divider.one { top: 838px; }
  .divider.two { top: 980px; }
  .footer { position: absolute; left: 0; top: 1087px; width: 934px; height: 113px; }
  .footer .phone-block {
    position: absolute; left: 0; top: 0; width: 379px; height: 113px;
    background: var(--orange); display: flex; align-items: center; padding-left: 47px; gap: 6px;
    color: var(--paper); font-family: "Roboto Condensed", Arial, sans-serif;
    font-weight: 700; font-size: 38px;
  }
  .footer .address-block {
    position: absolute; left: 364px; top: 0; width: 570px; height: 113px;
    background: var(--teal);
    clip-path: polygon(15px 0, 100% 0, 100% 100%, 15px 100%, 15px 62px, 0 56px, 15px 50px);
    display: flex; align-items: center; padding-left: 50px; gap: 8px;
    color: var(--paper); font-family: "Roboto Condensed", Arial, sans-serif; font-size: 23px;
  }
</style>
</head>
<body>
  <main class="flyer">
    <div class="hero-photo" role="img" aria-label="Close-up photo of a smiling woman with white teeth against a light blue background"></div>
    <div class="accent-band"></div>

    <div class="map-badge">
      <div class="map-frame">
        <div class="map-area" role="img" aria-label="Street map showing the clinic location in Huntington Beach"></div>
      </div>
    </div>

    <div class="brand">
      <span class="brand-mark"></span>
      <span class="brand-name">Daybreak Dental</span>
    </div>
    <p class="brand-doctor">Lena Harper, DDS</p>

    <h1 class="headline grand">GRAND</h1>
    <h1 class="headline opening">OPENING</h1>

    <div class="offer exam">
      <span class="offer-key">$50</span>
      <span class="offer-text">Exam with Xrays &amp;<br>Cleaning <span class="offer-note">(regular)</span></span>
    </div>
    <div class="divider one"></div>

    <div class="offer bleach">
      <span class="offer-key">FREE</span>
      <span class="offer-text">BLEACHING<span class="offer-note">(after completion of dental treatment)</span></span>
    </div>
    <div class="divider two"></div>

    <div class="offer plans">
      <span class="offer-key">welcomed</span>
      <span class="offer-text">PPO, HMO, DentiCal</span>
    </div>

    <footer class="footer">
      <div class="phone-block">
        <svg width="36" height="36" viewBox="0 0 36 36" aria-hidden="true">
          <circle cx="18" cy="18" r="16" fill="none" stroke="#fff" stroke-width="3"/>
          <path d="M12 9c1-1 2-1 3 0l2 3c.6 1 .4 2-.4 2.6l-1.2 1c1 2.2 2.6 3.8 4.8 4.8l1-1.2c.6-.8 1.6-1 2.6-.4l3 2c1 1 1 2 0 3l-1.4 1.4c-1.4 1.4-4 1-7-1.2-3-2.2-5.4-5-6.6-8-1-2.4-.8-4.6.4-5.8z" fill="#fff"/>
        </svg>
        <span>(714) 555-0182</span>
      </div>
      <div class="address-block">
        <svg width="18" height="24" viewBox="0 0 18 24" aria-hidden="true">
          <path d="M9 1a7 7 0 0 0-7 7c0 5.2 7 14 7 14s7-8.8 7-14a7 7 0 0 0-7-7z" fill="#fff"/>
          <circle cx="9" cy="8" r="2.6" fill="#00a0b0"/>
        </svg>
        <span>4820 Harbor Ave., Huntington Beach, CA 92649</span>
      </div>
    </footer>
  </main>
</body>
</html>
```